shop signs for newquay all year round

We require a shop front signage
2 x 2.5m Long by 1.5m High (sides)
1 x 8m long by 0.7m High (front)

The front sign must read - Penny Wise Bargain Store with the last 1.5m showing the the Xmas Shop open all year (see image 1)

The side signs must have a big bold Arrow pointing Left and one Pointing Right with the words Clearance Sale Now On (see image 2)

Colors

Designer to choose colors to be used in the design.

Requirements
Must have
• signs must be bold and clear to get shoppers into the store, it must be bright and stand out
Nice to have
• good graphics and artwork
Should not have
• plain text

```html
<!DOCTYPE html>
<html lang="en">
<head>
<meta charset="utf-8">
<title>Penny Wise Bargain Store – Shop Signage</title>
<link rel="stylesheet" href="https://fonts.googleapis.com/css2?family=Montserrat:wght@400;500;700;800&display=swap">
<style>
  :root {
    --wall: #e6e6e6;
    --red-deep: #9c1226;
    --red-bright: #c9163b;
    --red-dark: #6e0a14;
    --white: #ffffff;
    --arrow: #b3142e;
    --shadow: rgba(0, 0, 0, 0.28);
  }
  * { margin: 0; padding: 0; box-sizing: border-box; }
  html, body { width: 1200px; height: 1000px; overflow: hidden; }
  body {
    background: var(--wall);
    font-family: "Montserrat", Arial, sans-serif;
    position: relative;
  }
  .red-fill {
    background: linear-gradient(90deg, var(--red-deep) 0%, var(--red-bright) 30%, var(--red-deep) 55%, var(--red-bright) 80%, var(--red-deep) 100%);
  }
  .fascia {
    position: absolute;
    left: 58px; top: 205px;
    width: 1085px; height: 136px;
    box-shadow: 0 3px 8px var(--shadow);
    display: flex;
  }
  .fascia__name {
    flex: 1;
    display: flex;
    align-items: center;
    padding-left: 34px;
    color: var(--white);
    font-weight: 500;
    font-size: 53px;
    letter-spacing: -0.5px;
    white-space: nowrap;
  }
  .fascia__xmas {
    width: 205px;
    height: 100%;
    position: relative;
    background: radial-gradient(circle at 50% 35%, #f07a86 0%, #d8263e 35%, #9a0e1c 75%), var(--red-dark);
  }
  .fascia__xmas-art {
    position: absolute; inset: 0 0 36px 0;
    background:
      radial-gradient(ellipse at 20% 0%, #2f6b2a 0%, rgba(47,107,42,0) 45%),
      radial-gradient(ellipse at 85% 0%, #2f6b2a 0%, rgba(47,107,42,0) 50%),
      radial-gradient(circle at 50% 45%, #f5b0b6 0%, rgba(230,60,80,0) 55%);
  }
  .fascia__xmas-text {
    position: absolute;
    left: 0; right: 0; bottom: 0;
    padding: 0 0 8px 10px;
    color: var(--white);
    background: linear-gradient(180deg, rgba(110,10,20,0) 0%, var(--red-dark) 45%);
  }
  .fascia__xmas-title { font-size: 18px; font-weight: 400; line-height: 22px; }
  .fascia__xmas-open { font-size: 18px; font-weight: 800; line-height: 22px; }

  .side-sign {
    position: absolute;
    top: 365px;
    width: 476px; height: 376px;
    box-shadow: 0 3px 8px var(--shadow);
    color: var(--white);
    text-align: center;
  }
  .side-sign--left { left: 61px; }
  .side-sign--right { left: 665px; }
  .side-sign__headline {
    position: absolute; left: 0; right: 0; top: 42px;
    font-weight: 800;
    font-size: 60px;
    line-height: 56px;
    letter-spacing: -0.5px;
  }
  .side-sign__sub {
    position: absolute; left: 0; right: 0; top: 187px;
    font-weight: 400;
    font-size: 46px;
    line-height: 50px;
  }
  .side-sign__band {
    position: absolute; left: 0; top: 267px;
    width: 476px; height: 80px;
    background: var(--white);
  }
  .side-sign__band svg { display: block; }
  .arrow { fill: var(--arrow); }
</style>
</head>
<body>
  <header class="fascia red-fill">
    <div class="fascia__name">Penny Wise Bargain Store</div>
    <div class="fascia__xmas">
      <div class="fascia__xmas-art" role="img" aria-label="Christmas baubles hanging from pine branches with sparkling red lights"></div>
      <div class="fascia__xmas-text">
        <div class="fascia__xmas-title">Xmas Shop</div>
        <div class="fascia__xmas-open">OPEN ALL YEAR</div>
      </div>
    </div>
  </header>

  <section class="side-sign side-sign--left red-fill">
    <div class="side-sign__headline">CLEARANCE<br>SALE</div>
    <div class="side-sign__sub">NOW ON</div>
    <div class="side-sign__band">
      <svg width="476" height="80" viewBox="0 0 476 80" aria-label="Arrow pointing left">
        <polygon class="arrow" points="150,41 188,13 198,13 165,41 198,69 188,69"/>
        <polygon class="arrow" points="166,41 226,8 226,29 343,29 343,53 226,53 226,74"/>
      </svg>
    </div>
  </section>

  <section class="side-sign side-sign--right red-fill">
    <div class="side-sign__headline">CLEARANCE<br>SALE</div>
    <div class="side-sign__sub">NOW ON</div>
    <div class="side-sign__band">
      <svg width="476" height="80" viewBox="0 0 476 80" aria-label="Arrow pointing right">
        <polygon class="arrow" points="326,41 288,13 278,13 311,41 278,69 288,69"/>
        <polygon class="arrow" points="310,41 250,8 250,29 133,29 133,53 250,53 250,74"/>
      </svg>
    </div>
  </section>
</body>
</html>
```